Kestrel Dawn Magazine need Logo desing and front page for 1 edittion

This is a new magazine that will be circulating in Panama. the magazine will run non for profit,will be mostly informative and few advertizers to cover printing costs.
the magaine will oncce every 2 or 3 month. we need to present it to the editors who will be aproving or diss aproving the project.

we need a Logo desing for the name of the magazine "Kestrel Dawn" and the "front cover desing for the first edition" it will be good if the designer can incude the designed format for the iner magazine, for us just to add in the artucles and the spaces for advertizing.

the magazine content will be articles by govenment energy sectors, gloval warming articles, articles in renewvable enery, university profesor talking or promoting new ideas or university advances, orientations, special edition on book or international articles about the subject on saving enerty, different sectors, world innovations in renewbable energy, and the companies who will advertize will be comapnies selling VRAX products, companies offfering product and services on renewvable energy, Led product and systems companies etc...

```html
<!DOCTYPE html>
<html lang="en">
<head>
<meta charset="utf-8">
<title>Kestrel Dawn — Inner Spread</title>
<link rel="stylesheet" href="https://fonts.googleapis.com/css2?family=Arimo:wght@400;700&family=Poiret+One&display=swap">
<style>
  :root {
    --backdrop: #e8e8e8;
    --paper: #ffffff;
    --ink: #3f3f3f;
    --ink-soft: #6b6b6b;
    --quote: #4f6677;
    --spine: #1a1a1a;
    --sky-top: #6f8196;
    --sky-mid: #a9b4c1;
    --sky-glow: #e3cdbd;
    --treeline: #1e1c1e;
  }
  * { box-sizing: border-box; margin: 0; padding: 0; }
  html, body {
    width: 1200px; height: 1000px; overflow: hidden;
    background: var(--backdrop);
  }
  .canvas { position: relative; width: 1200px; height: 1000px; }
  .spread {
    position: absolute; left: 22px; top: 125px;
    width: 1154px; height: 743px;
    background: var(--paper);
  }
  .running-head {
    position: absolute; top: 31px;
    font-family: "Arimo", Arial, sans-serif;
    font-size: 10px; letter-spacing: .3px;
    color: var(--ink-soft); text-transform: uppercase;
  }
  .running-head b { color: var(--ink); font-weight: 700; }
  .running-head .sep { margin: 0 6px; }
  .running-head--left { left: 33px; }
  .running-head--right { right: 36px; }
  .spine { position: absolute; left: 575px; top: 8px; width: 6px; height: 730px; }
  .feature-photo {
    position: absolute; left: 33px; top: 78px; width: 510px; height: 316px;
    background: linear-gradient(180deg, var(--sky-top) 0%, var(--sky-mid) 45%, var(--sky-glow) 70%, #7d7c86 82%, var(--treeline) 92%);
  }
  .pull-quote {
    position: absolute; left: 33px; top: 428px; width: 340px;
    font-family: "Poiret One", "Century Gothic", sans-serif;
    font-size: 25.5px; line-height: 30px; letter-spacing: 2.2px;
    color: var(--quote);
  }
  .column {
    position: absolute; overflow: hidden;
    font-family: "Arimo", Arial, sans-serif;
    font-size: 8.2px; line-height: 12.2px; color: var(--ink);
  }
  .column p + p { margin-top: 11px; }
  .col-l1 { left: 33px;  top: 572px; width: 155px; height: 110px; }
  .col-l2 { left: 210px; top: 572px; width: 160px; height: 110px; }
  .col-l3 { left: 388px; top: 430px; width: 157px; height: 252px; }
  .col-r1 { left: 606px; top: 76px;  width: 163px; height: 606px; }
  .col-r2 { left: 781px; top: 76px;  width: 164px; height: 606px; }
  .col-r3 { left: 955px; top: 76px;  width: 164px; height: 606px; }
</style>
</head>
<body>
<div class="canvas">
  <article class="spread">
    <header class="running-head running-head--left"><b>6</b><span class="sep">|</span>Kestrel Dawn</header>
    <header class="running-head running-head--right">January 2014<span class="sep">|</span><b>7</b></header>

    <svg class="spine" viewBox="0 0 6 730" aria-hidden="true">
      <line x1="3" y1="0" x2="3" y2="730" stroke="var(--spine)" stroke-width="3" stroke-dasharray="30 38"/>
    </svg>

    <div class="feature-photo" role="img" aria-label="Photo of high-voltage transmission towers silhouetted against a cloudy dusk sky above a dark treeline"></div>

    <blockquote class="pull-quote">“Renewable energy is one of the fastest growing sectors of the global economy.”</blockquote>

    <div class="column col-l1">
      <p>Solar farms across the isthmus now feed power into the national grid during the dry season, when rivers run low and demand climbs. Engineers say the new lines carry more load with fewer losses, and towns are starting to see steadier supply and lower bills through the year.</p>
    </div>
    <div class="column col-l2">
      <p>Wind studies on the Pacific coast show strong, reliable breezes from December to April. Planners hope to pair these sites with hydro stations so that one source can cover the other, keeping the system balanced through each season and every storm that passes over the hills.</p>
    </div>
    <div class="column col-l3">
      <p>across the region. Universities are training a new group of technicians who can install, test and repair panels, inverters and storage units in rural schools and clinics. Many of these graduates return to their home provinces, where they set up small firms and teach neighbours how to read meters and plan their use of power. The ministry has promised grants for pilot projects that show clear savings within two years, and several cooperatives have already applied. Farmers who pump water with sunlight say the change has cut fuel costs by half and freed time for other work. Critics warn that the grid still needs heavy investment before it can accept large flows from many small producers, and that rules for selling power back remain unclear. Still, the mood among builders and buyers is hopeful, and new orders arrive every month.</p>
    </div>

    <div class="column col-r1">
      <p>ing in coastal cities, where air conditioning drives most of the daily peak. Building owners are testing reflective roofs, shaded windows and smart thermostats that shift cooling to cheaper hours without making rooms less comfortable.</p>
      <p>Early results from three office towers suggest a drop of nearly one fifth in monthly use.</p>
      <p>Lighting is another quick win. Replacing old tubes with efficient lamps pays back in months, and many schools now run on a fraction of the power they needed a decade ago.</p>
      <p>Banks have begun to offer small loans for home systems, with payments set close to what families already spend on electricity. Installers report that interest grew sharply once neighbours could see working panels on nearby roofs and hear first-hand how little upkeep they need.</p>
      <p>Storage remains the hardest piece of the puzzle. Batteries are getting cheaper, yet they still add a large share to the cost of a full system. Researchers at the national university are studying ways to store heat and pumped water instead, using hills and reservoirs that already exist near several plants. Their models show that a modest reservoir could hold enough energy to carry a mid-sized town through the evening peak, when solar output fades and demand rises as families return home. The team plans a field trial next year with support from local councils and two private partners who supply the pumps and control software. If the test succeeds, the method could be copied in other valleys with similar terrain and steady rainfall.</p>
    </div>
    <div class="column col-r2">
      <p>Transport is the next frontier. City buses powered by electricity are quieter and cleaner, and drivers say they are easier to handle in heavy traffic. Operators still worry about range on long routes, so the first lines will run short loops through the centre where charging points are close at hand.</p>
      <p>Ports and canals also play a role. Ships waiting at anchor burn fuel to keep lights and pumps running, and shore power could cut that waste. Port managers are studying how much new capacity they would need and who should pay for it.</p>
      <p>Public awareness has grown fast. Schools hold energy fairs where pupils build small turbines and solar ovens, and radio programmes explain how to read a bill and spot waste at home.</p>
      <p>Local councils are drafting codes that ask new buildings to include shading, natural airflow and space for panels on the roof.</p>
      <p>Experts agree that policy must stay steady. Investors need to know that rules will hold for many years before they commit large sums to wind farms or new lines. A clear plan with firm targets, fair prices and simple permits would do more than any single subsidy, they argue, and would let smaller firms compete alongside the large utilities. Several business groups have asked for a public forum to shape the next national plan, and officials have signalled that they are open to the idea.</p>
    </div>
    <div class="column col-r3">
      <p>Abroad, neighbours are moving quickly. Regional links would let countries trade surplus power at different hours, smoothing out the peaks that strain each grid on its own. Talks on shared lines have resumed after a long pause, and engineers are mapping possible routes along existing roads.</p>
      <p>Such links could also help during droughts, when hydro output falls and prices rise. A wider market spreads the risk and keeps supply steady for homes and factories alike.</p>
      <p>Water and energy are closely tied. Dams supply much of the country's power, yet they also feed farms, cities and the canal itself. Careful planning is needed so that no single use takes more than its share in a dry year, and so that rivers keep enough flow for fish and forests downstream. Scientists are building better forecasts of rainfall to guide these choices well in advance.</p>
      <p>Forests matter too. Healthy watersheds hold rain and release it slowly, which keeps reservoirs full through the long dry months and protects turbines from silt.</p>
      <p>Looking ahead, the sector expects steady growth. New jobs in design, installation and maintenance are opening across the provinces, and training centres report full classes for the coming term. Leaders hope this momentum will turn early pilot projects into a lasting network of clean, affordable power that serves every community, from the busy capital to the most distant mountain village, for many years to come.</p>
    </div>
  </article>
</div>
</body>
</html>
```